PowerPoint Corporate Template for Healthcare AI Technology Company

Take logo and create a comprehensive source file for corporate PowerPoint presentation library that provides an array of title/separator slides, graphic presentation options, chart options and text slide options. Utilize the current logo files and provide options on white backgrounds, and knock out options.

Target Market(s)

Pharmaceutical Manufacturers

Font styles to use
Sans Serif

Colors
6b449b
0556a4
33a6d7
0393ce
ffffff
e34197

Requirements
Must have
• Use logos upgraded in files; create an embedded color palette that aligns to the logo; include multiple options for different types of slides including charts; create a bullet point that is the logo in the purple/blue color with white background; incorporate knock out logo version option for separator pages; must include page numbers; use font aligned to logo for text slide options
Nice to have
• Tech looking, data intensive slide options that communicate easily; could be using 3-4 data points per slide
Should not have
• Any logo other than what has been shared

```html
<!DOCTYPE html>
<html lang="en">
<head>
<meta charset="utf-8">
<title>Veritana Presentation Template Overview</title>
<link href="https://fonts.googleapis.com/css2?family=Roboto:wght@300;400;700&display=swap" rel="stylesheet">
<style>
:root{
  --purple:#6b449b;
  --navy:#0556a4;
  --sky:#33a6d7;
  --cyan:#0393ce;
  --pink:#e34197;
  --white:#ffffff;
  --canvas:#acacac;
  --panel:#6b6b6b;
  --panel-dark:#5a5a5a;
  --ruler:#8a8a8a;
  --ink:#1a1a1a;
}
*{box-sizing:border-box;margin:0;padding:0}
html,body{width:1200px;height:1200px;overflow:hidden}
body{background:var(--canvas);font-family:"Roboto",Arial,sans-serif;position:relative}
.abs{position:absolute}
.section-heading{position:absolute;left:37px;color:var(--white);font-weight:700;font-size:21px;letter-spacing:-.2px}

/* Editor window */
.editor{position:absolute;left:284px;top:24px;width:631px;height:306px;background:var(--panel)}
.thumb-pane{position:absolute;left:0;top:0;width:122px;height:306px;background:var(--panel)}
.thumb-scroll{position:absolute;left:113px;top:0;width:9px;height:306px;background:var(--panel-dark)}
.thumb-scroll::after{content:"";position:absolute;left:2px;top:10px;width:5px;height:140px;background:#9a9a9a}
.thumb-num{position:absolute;left:8px;color:#e8e8e8;font-size:8px}
.thumb{position:absolute;left:17px;width:83px;height:47px;overflow:hidden;border:1px solid #444}
.thumb.active{outline:1.5px solid #e2562a}
.ruler-top{position:absolute;left:148px;top:2px;width:467px;height:10px;background:var(--ruler);font-size:6px;color:#f0f0f0;display:flex;justify-content:space-between;align-items:center;padding:0 6px}
.ruler-left{position:absolute;left:127px;top:19px;width:10px;height:262px;background:var(--ruler)}
.stage-scroll{position:absolute;left:619px;top:0;width:10px;height:300px;background:var(--panel-dark)}
.stage-scroll::after{content:"";position:absolute;left:2px;top:12px;width:6px;height:20px;background:#9a9a9a}
.notes{position:absolute;left:122px;top:287px;width:509px;height:19px;background:var(--panel);border-top:1px solid #575757;color:#eaeaea;font-size:8.5px;padding:3px 7px}

/* Title slide */
.title-slide{position:absolute;width:539px;height:303px;overflow:hidden}
.title-photo{position:absolute;inset:0}
.photo-lab{background:linear-gradient(100deg,#45a9dc 0%,#56b3df 45%,#8cc6e2 70%,#b9d6e3 100%)}
.photo-pills{background:linear-gradient(100deg,#46aadc 0%,#4eaedd 50%,#9cd3e6 72%,#d8ece9 86%,#e2b89a 100%)}
.wordmark-lg{position:absolute;left:23px;top:124px;display:flex;align-items:center}
.wordmark-lg .mark{width:54px;height:54px;border:3px solid var(--white);border-radius:50%}
.wordmark-lg .name{margin-left:20px;font-weight:300;font-size:54px;color:var(--white);letter-spacing:-.5px;line-height:1}
.title-field{position:absolute;left:81px;top:187px;right:0;height:50px;border:1px dotted rgba(255,255,255,.75);border-right:none;color:var(--white);font-size:16px;padding:15px 0 0 5px}

/* Divider slide */
.divider{position:absolute;width:309px;height:174px;overflow:hidden;transform-origin:0 0}
.divider .mark{position:absolute;left:9px;top:73px;width:33px;height:33px;border:2px solid var(--white);border-radius:50%}
.divider .field{position:absolute;left:45px;top:73px;right:0;height:34px;border:1px solid rgba(255,255,255,.3);border-right:none;color:var(--white);font-size:13.5px;padding:8px 0 0 3px}
.bg-pink{background:var(--pink)} .bg-purple{background:var(--purple)} .bg-navy{background:var(--navy)} .bg-cyan{background:var(--cyan)} .bg-sky{background:var(--sky)}

/* Content layout slide */
.layout{position:absolute;width:364px;height:203px;background:var(--white);overflow:hidden;transform-origin:0 0}
.layout .brand{position:absolute;right:12px;top:11px;display:flex;align-items:center}
.layout .brand .mark{width:19px;height:19px;border:1.5px solid var(--purple);border-radius:50%}
.layout .brand .name{margin-left:4px;font-weight:300;font-size:17px;color:var(--purple);line-height:1}
.layout .rule{position:absolute;left:0;top:38px;width:350px;height:1px;background:#b9b9b9}
.layout .band{position:absolute;left:0;bottom:0;width:100%;height:14px;background:var(--purple)}
.box{position:absolute;border:1px dotted #9b9b9b}
.title-box{color:var(--purple);font-size:14px;padding:2px 3px}
.body-box{font-size:10.5px;color:var(--ink);padding:2px 3px}
.lvl{display:flex;align-items:center;line-height:1.35;white-space:nowrap}
.lvl::before{content:"";width:5px;height:5px;border:1px solid var(--sky);border-radius:50%;margin-right:2px;flex:none}
.l2{margin-left:13px;font-size:9.5px}
.l3{margin-left:27px;font-size:7.5px}
.l4{margin-left:41px;font-size:7px}
.l5{margin-left:55px;font-size:7px}
.icons{position:absolute}
.pic-label{font-size:12px;color:var(--ink);padding:2px 3px}
.pic-icon{position:absolute;left:56px;top:55px;width:12px;height:12px;border:1px solid #c9c9c9;background:#eef4fa}

/* Thumbnail content */
.lorem-head{position:absolute;left:9px;top:46px;font-size:12px;color:var(--purple)}
.lorem-list{position:absolute;top:70px;font-size:9px;color:#333;line-height:1.45}
.lorem-photo{position:absolute;left:230px;top:68px;width:110px;height:90px;background:linear-gradient(135deg,#6b8aa0,#c7d3dc)}
</style>
</head>
<body>

<!-- Editor view -->
<section class="editor" aria-label="Presentation editor view">
  <div class="thumb-pane">
    <span class="thumb-num" style="top:12px">1</span>
    <div class="thumb active" style="top:20px">
      <div class="title-slide" style="transform:scale(.154);transform-origin:0 0">
        <div class="title-photo photo-lab" role="img" aria-label="Photo of a scientist in a protective suit working at a microscope"></div>
        <div class="wordmark-lg"><span class="mark"></span><span class="name">Veritana</span></div>
        <div class="title-field"></div>
      </div>
    </div>
    <span class="thumb-num" style="top:72px">2</span>
    <div class="thumb" style="top:80px">
      <div class="divider bg-pink" style="transform:scale(.269)"><span class="mark"></span></div>
    </div>
    <span class="thumb-num" style="top:132px">3</span>
    <div class="thumb" style="top:140px">
      <div class="layout" style="transform:scale(.228)">
        <div class="brand"><span class="mark"></span><span class="name">Veritana</span></div>
        <div class="rule"></div>
        <div class="lorem-head">Lorem ipsum dolor sit amet</div>
        <div class="lorem-list" style="left:14px">Consectetur adipiscing elit<br>Sed do eiusmod tempor<br>Incididunt ut labore et<br>Dolore magna aliqua</div>
        <div class="band"></div>
      </div>
    </div>
    <span class="thumb-num" style="top:192px">4</span>
    <div class="thumb" style="top:200px">
      <div class="layout" style="transform:scale(.228)">
        <div class="brand"><span class="mark"></span><span class="name">Veritana</span></div>
        <div class="rule"></div>
        <div class="lorem-head">Lorem ipsum dolor sit amet</div>
        <div class="lorem-list" style="left:14px">Consectetur adipiscing elit<br>Sed do eiusmod tempor<br>Incididunt ut labore et<br>Dolore magna aliqua</div>
        <div class="lorem-list" style="left:190px">Consectetur adipiscing elit<br>Sed do eiusmod tempor<br>Incididunt ut labore et<br>Dolore magna aliqua</div>
        <div class="band"></div>
      </div>
    </div>
    <span class="thumb-num" style="top:252px">5</span>
    <div class="thumb" style="top:260px">
      <div class="layout" style="transform:scale(.228)">
        <div class="brand"><span class="mark"></span><span class="name">Veritana</span></div>
        <div class="rule"></div>
        <div class="lorem-head">Lorem ipsum dolor sit amet</div>
        <div class="lorem-list" style="left:14px">Consectetur adipiscing elit<br>Sed do eiusmod tempor<br>Incididunt ut labore et<br>Dolore magna aliqua<br>Ut enim ad<br>Quis nostrud</div>
        <div class="lorem-photo" role="img" aria-label="Photo of a scientist at a microscope"></div>
        <div class="band"></div>
      </div>
    </div>
    <div class="thumb-scroll"></div>
  </div>

  <div class="ruler-top"><span>16</span><span>14</span><span>12</span><span>10</span><span>8</span><span>6</span><span>4</span><span>2</span><span>0</span><span>2</span><span>4</span><span>6</span><span>8</span><span>10</span><span>12</span><span>14</span><span>16</span></div>
  <div class="ruler-left"></div>

  <div class="title-slide" style="left:147px;top:19px;transform:scale(.863);transform-origin:0 0">
    <div class="title-photo photo-lab" role="img" aria-label="Photo of a scientist in a protective suit working at a microscope"></div>
    <div class="wordmark-lg"><span class="mark"></span><span class="name">Veritana</span></div>
    <div class="title-field">Click to add title</div>
  </div>
  <div class="stage-scroll"></div>
  <div class="notes">Click to add notes</div>
</section>

<!-- Title slides -->
<h2 class="section-heading" style="top:346px">Title slide options</h2>

<div class="title-slide" style="left:37px;top:381px">
  <div class="title-photo photo-lab" role="img" aria-label="Photo of a scientist in a protective suit working at a microscope, tinted blue"></div>
  <div class="wordmark-lg"><span class="mark"></span><span class="name">Veritana</span></div>
  <div class="title-field">Click to add title</div>
</div>

<div class="title-slide" style="left:626px;top:381px;width:537px">
  <div class="title-photo photo-pills" role="img" aria-label="Photo of capsules spilling from a pill bottle, tinted blue"></div>
  <div class="wordmark-lg"><span class="mark"></span><span class="name">Veritana</span></div>
  <div class="title-field">Click to add title</div>
</div>

<!-- Divider slides -->
<h2 class="section-heading" style="top:700px">Divider slide options</h2>

<div class="divider bg-pink" style="left:37px;top:736px"><span class="mark"></span><div class="field">Click to add title</div></div>
<div class="divider bg-purple" style="left:358px;top:768px;transform:scale(.634)"><span class="mark"></span><div class="field">Click to add title</div></div>
<div class="divider bg-navy" style="left:565px;top:768px;transform:scale(.634)"><span class="mark"></span><div class="field">Click to add title</div></div>
<div class="divider bg-cyan" style="left:771px;top:768px;transform:scale(.634)"><span class="mark"></span><div class="field">Click to add title</div></div>
<div class="divider bg-sky" style="left:977px;top:768px;transform:scale(.634)"><span class="mark"></span><div class="field">Click to add title</div></div>

<!-- Layout slides -->
<h2 class="section-heading" style="top:927px">Slide layout options</h2>

<svg width="0" height="0" style="position:absolute">
  <defs>
    <g id="content-icons">
      <rect x="0" y="0" width="12" height="10" fill="#fff" stroke="#a9a9a9" stroke-width=".8"/>
      <line x1="0" y1="4" x2="12" y2="4" stroke="#a9a9a9" stroke-width=".6"/>
      <rect x="18" y="3" width="3" height="7" fill="#e0b34a"/><rect x="22" y="0" width="3" height="10" fill="#6f9fd8"/><rect x="26" y="5" width="3" height="5" fill="#e0b34a"/>
      <polygon points="34,0 44,0 46,5 36,5" fill="#7fb38f"/><rect x="36" y="5" width="10" height="5" fill="#fff" stroke="#a9a9a9" stroke-width=".6"/>
      <rect x="0" y="15" width="12" height="10" fill="#eef4fa" stroke="#a9a9a9" stroke-width=".8"/>
      <rect x="17" y="15" width="12" height="10" fill="#fff" stroke="#a9a9a9" stroke-width=".8"/><rect x="19" y="20" width="3" height="5" fill="#6f9fd8"/>
      <rect x="34" y="15" width="12" height="10" fill="#fff" stroke="#a9a9a9" stroke-width=".8"/><circle cx="43" cy="22" r="3" fill="none" stroke="#a9a9a9" stroke-width=".6"/>
    </g>
  </defs>
</svg>

<div class="layout" style="left:37px;top:963px">
  <div class="brand"><span class="mark"></span><span class="name">Veritana</span></div>
  <div class="rule"></div>
  <div class="box title-box" style="left:12px;top:53px;width:338px;height:36px">Click to edit Master title style</div>
  <div class="box body-box" style="left:12px;top:88px;width:338px;height:88px">
    <div class="lvl">Edit Master text styles</div>
    <div class="lvl l2">Second level</div>
    <div class="lvl l3">Third level</div>
    <div class="lvl l4">Fourth level</div>
    <div class="lvl l5">Fifth level</div>
  </div>
  <svg class="icons" style="left:158px;top:122px" width="48" height="26" aria-hidden="true"><use href="#content-icons"/></svg>
  <div class="band"></div>
</div>

<div class="layout" style="left:423px;top:963px">
  <div class="brand"><span class="mark"></span><span class="name">Veritana</span></div>
  <div class="rule"></div>
  <div class="box title-box" style="left:13px;top:53px;width:338px;height:36px">Click to edit Master title style</div>
  <div class="box body-box" style="left:13px;top:88px;width:158px;height:88px">
    <div class="lvl">Edit Master text styles</div>
    <div class="lvl l2">Second level</div>
    <div class="lvl l3">Third level</div>
    <div class="lvl l4">Fourth level</div>
    <div class="lvl l5">Fifth level</div>
  </div>
  <div class="box body-box" style="left:192px;top:88px;width:158px;height:88px">
    <div class="lvl">Edit Master text styles</div>
    <div class="lvl l2">Second level</div>
    <div class="lvl l3">Third level</div>
    <div class="lvl l4">Fourth level</div>
    <div class="lvl l5">Fifth level</div>
  </div>
  <svg class="icons" style="left:67px;top:122px" width="48" height="26" aria-hidden="true"><use href="#content-icons"/></svg>
  <svg class="icons" style="left:246px;top:122px" width="48" height="26" aria-hidden="true"><use href="#content-icons"/></svg>
  <div class="band"></div>
</div>

<div class="layout" style="left:808px;top:963px">
  <div class="brand"><span class="mark"></span><span class="name">Veritana</span></div>
  <div class="rule"></div>
  <div class="box title-box" style="left:13px;top:53px;width:191px;height:36px">Click to edit Master title style</div>
  <div class="box body-box" style="left:13px;top:88px;width:191px;height:88px">
    <div class="lvl">Edit Master text styles</div>
    <div class="lvl l2">Second level</div>
    <div class="lvl l3">Third level</div>
    <div class="lvl l4">Fourth level</div>
    <div class="lvl l5">Fifth level</div>
  </div>
  <svg class="icons" style="left:86px;top:122px" width="48" height="26" aria-hidden="true"><use href="#content-icons"/></svg>
  <div class="box" style="left:224px;top:53px;width:126px;height:122px">
    <div class="pic-label">Picture</div>
    <span class="pic-icon"></span>
  </div>
  <div class="band"></div>
</div>

</body>
</html>
```